Book Cover : Silent Helix Remedy: Our Rewritten Borderland

We need a striking and engaging book cover for this new book which describes the development of the COVID-19 vaccine technology and it's potential to change the world in ways which most people don't yet realise.

On the book cover we need to include:

Silent Helix Remedy: Our Rewritten Borderland

Safety/Efficiency/Future Applications/CRISPR

Bartosz Wileński

```html
<!DOCTYPE html>
<html lang="en">
<head>
<meta charset="utf-8">
<title>Silent Helix Remedy: Our Rewritten Borderland — Book Cover</title>
<link rel="stylesheet" href="https://fonts.googleapis.com/css2?family=Oswald:wght@500;600&display=swap">
<style>
  :root {
    --ember-deep: #6e1f12;
    --ember-mid: #b8361c;
    --ember-bright: #e2562a;
    --flame: #f08a1e;
    --title-white: #ffffff;
    --title-shadow: #272c38;
    --band-navy: #262d38;
  }
  * { margin: 0; padding: 0; box-sizing: border-box; }
  html, body { width: 800px; height: 1200px; overflow: hidden; background: var(--band-navy); }
  .cover {
    position: relative;
    width: 800px;
    height: 1200px;
    overflow: hidden;
    font-family: "Oswald", "Arial Narrow", sans-serif;
  }
  .cover-art {
    position: absolute;
    inset: 0 0 89px 0;
    background:
      radial-gradient(ellipse 55% 40% at 22% 72%, rgba(240,138,30,0.55), transparent 70%),
      radial-gradient(ellipse 60% 30% at 70% 88%, rgba(240,120,30,0.45), transparent 70%),
      radial-gradient(ellipse 50% 25% at 30% 5%, rgba(226,86,42,0.6), transparent 70%),
      linear-gradient(170deg, var(--ember-mid) 0%, var(--ember-deep) 35%, var(--ember-mid) 60%, var(--ember-bright) 85%, var(--flame) 100%);
  }
  .series-line {
    position: absolute;
    top: 56px;
    left: 70px;
    width: 646px;
    color: var(--title-white);
    font-weight: 500;
    font-size: 29px;
    letter-spacing: 4.6px;
    white-space: nowrap;
  }
  .book-title {
    position: absolute;
    top: 128px;
    right: 70px;
    text-align: right;
    color: var(--title-white);
    font-weight: 600;
    font-size: 128px;
    line-height: 126px;
    letter-spacing: -1px;
    text-shadow: 4px 4px 0 var(--title-shadow);
  }
  .book-title span { display: block; }
  .author-band {
    position: absolute;
    left: 0; right: 0; bottom: 0;
    height: 89px;
    background: var(--band-navy);
    display: flex;
    align-items: center;
    justify-content: center;
  }
  .author-name {
    color: var(--title-white);
    font-weight: 600;
    font-size: 56px;
    line-height: 1;
    margin-top: -4px;
  }
</style>
</head>
<body>
  <main class="cover">
    <div class="cover-art" role="img" aria-label="Illustration of a red coronavirus particle among glowing orange RNA strands and tubes on a fiery red background"></div>
    <p class="series-line">Safety/Efficiency/Future Applications/CRISPR</p>
    <h1 class="book-title">
      <span>Silent</span>
      <span>Helix</span>
      <span>Remedy:</span>
      <span>Our</span>
      <span>Rewritten</span>
      <span>Borderland</span>
    </h1>
    <footer class="author-band">
      <p class="author-name">Bartosz Wileński</p>
    </footer>
  </main>
</body>
</html>
```